Wordpress Design Project

I would like a Thesis-based Wordpress design for my site - BellowMarsh.com. The purpose of this site is to build a community that follow along on my journey from $0 to $100,000 in trading profits. The goal of the home page is to capture the viewer's email address. There will be a feature box with video of me and an opt-in to the right. I purchased a skin that I'm not happy with it, but you can get an idea of what I was trying to do by visiting the site now. You'll see that I already have the logo. The second most important thing to me is ease of navigation. There should be a prominent navigation bar underneath the feature box. See the nav bar at quietorchardlanes.com for an example. I'll be following a similar content strategy with a lot of educational posts and a separate page for podcasts and videos.
Updates
I just updated the brief to be more specific about the page elements and features I'm looking for. Hopefully this will answer most of the questions I've received so far.
Reason: I'm extending the deadline because I'll be on vacation for about 5 days and I want to make sure I have enough time to provide feedback and evaluate the designs. Thanks for everyone who has submitted so far - the designs look good.
Industry/Entity Type
Build
Requirements
Must have
- The front page will be the blog with the following from top to bottom:
1) BellowMarsh logo
2) Video and large email signup form (no name, just email address). I use Aweber for my email list if that makes a difference.
3) Navigation bar
All other pages will not have item 2 above, but should have an email signup form in the right side bar.
Right side bar functionality should mimic quietorchardlanes.com to include:
1) Email signup form
2) Multi-tab post menu that I can edit
3) Search box
4) Place to list foundation content links

```html
<!DOCTYPE html>
<html lang="en">
<head>
<meta charset="utf-8">
<title>BellowMarsh — About Us</title>
<link href="https://fonts.googleapis.com/css2?family=Montserrat:wght@300;400;500;600;700&family=Mulish:wght@400;600;700&display=swap" rel="stylesheet">
<style>
:root{
  --green:#4f9a1c;
  --green-dark:#3a7410;
  --green-light:#7cc33a;
  --ink:#1d1d1d;
  --text:#5a5a5a;
  --nav:#1f1f1f;
  --nav-2:#2e2e2e;
  --yellow:#f5b316;
  --orange:#f08a1c;
  --line:#e2e2e2;
  --page:#eeeeee;
  --white:#ffffff;
}
*{box-sizing:border-box;margin:0;padding:0}
html,body{width:1200px;height:2267px;overflow:hidden}
body{position:relative;font-family:"Mulish",sans-serif;color:var(--text);
  background:linear-gradient(#e6e6e6 0,#f7f7f7 700px,#ffffff 1200px,#ffffff 100%)}
.abs{position:absolute}

/* header */
.site-header{position:absolute;left:0;top:0;width:1200px;height:175px;
  background:linear-gradient(#f2f2f2,#fafafa)}
.social{position:absolute;top:6px;left:822px;display:flex;gap:14px}
.social span{width:28px;height:28px;border-radius:50%;background:#dfe6ee;border:1px solid #c9d2dc}
.brand{position:absolute;left:148px;top:50px;display:flex;align-items:center;gap:14px}
.brand .mark{width:86px;height:86px;border-radius:50%;background:var(--ink)}
.brand .name{font-family:"Montserrat",sans-serif;font-weight:500;font-size:52px;color:var(--ink);letter-spacing:-1px}
.membership{position:absolute;left:656px;top:74px;font-family:"Montserrat",sans-serif;color:var(--ink)}
.membership .l1{font-size:21px;font-weight:500}
.membership .l2{font-size:19px;font-weight:500;margin-top:2px}
.membership .l2 b{font-size:25px;font-weight:700}
.signup-strip{position:absolute;left:616px;top:132px;width:420px;height:43px;
  background:var(--green);border-radius:22px 22px 0 0}
.signup-strip .avatar{position:absolute;left:10px;top:2px;width:36px;height:36px;border-radius:50%;background:#e3a064}
.signup-strip .email{position:absolute;left:48px;top:7px;width:222px;height:28px;border-radius:14px;background:var(--white);
  font-size:14px;color:#6a6a6a;padding:5px 16px}
.signup-strip .btn{position:absolute;left:284px;top:5px;width:126px;height:32px;border-radius:16px;background:var(--yellow);
  font-family:"Montserrat",sans-serif;font-weight:700;font-size:16px;color:var(--ink);text-align:center;line-height:32px}

/* navigation */
.main-nav{position:absolute;left:0;top:175px;width:1200px;height:67px;border-top:5px solid var(--green);
  background:linear-gradient(var(--nav-2),var(--nav))}
.main-nav ul{list-style:none;display:flex;position:absolute;left:130px;top:0;height:62px}
.main-nav li{padding:10px 12px 0;border-right:1px solid #555;height:62px;color:#fff}
.main-nav li:last-child{border-right:0}
.main-nav .t{font-family:"Montserrat",sans-serif;font-size:17px;font-weight:500;text-transform:uppercase;letter-spacing:.3px}
.main-nav .s{font-size:11.5px;color:#cfcfcf;margin-top:1px}
.updates{position:absolute;top:248px;left:850px;font-size:12.5px;color:var(--ink);display:flex;align-items:center;gap:8px}
.updates a{color:#2c5fa8;text-decoration:none}
.updates .rss{width:16px;height:16px;background:var(--orange);border-radius:3px}

/* content */
.content-card{position:absolute;left:140px;top:271px;width:580px;height:848px;background:var(--white);
  border-radius:6px;box-shadow:0 1px 4px rgba(0,0,0,.12);padding:14px 28px}
.content-card h1{font-family:"Montserrat",sans-serif;font-weight:400;font-size:29px;color:var(--ink);margin-bottom:18px}
.content-card p{font-size:13.2px;line-height:19.8px;margin-bottom:19px}

/* sidebar */
.widget{position:absolute;left:745px;width:314px;background:var(--white);border-radius:6px}
.newsletter{top:271px;height:392px;border:1px solid #d6d6d6;box-shadow:0 2px 6px rgba(0,0,0,.12);text-align:center;padding-top:14px}
.newsletter h2{font-family:"Montserrat",sans-serif;font-weight:300;color:var(--green);font-size:27px;line-height:28px}
.newsletter h2 b{display:block;color:var(--ink);font-weight:600;font-size:33px;letter-spacing:1px;line-height:36px}
.newsletter .divider{position:absolute;left:22px;right:22px;top:118px;height:1px;background:#ccc}
.newsletter .icon{position:absolute;left:128px;top:90px;width:58px;height:58px;border-radius:50%;background:#fff;border:2px solid #ddd}
.newsletter p{position:absolute;left:32px;right:26px;top:160px;text-align:left;font-size:12.5px;line-height:19px;color:var(--ink)}
.newsletter .field{position:absolute;left:20px;top:242px;width:274px;height:42px;border:3px solid #c8c8c8;border-radius:4px;
  font-size:13px;line-height:36px;color:#888}
.newsletter .cta{position:absolute;left:38px;top:295px;width:236px;height:40px;border-radius:20px;
  background:linear-gradient(#8fd24a,#3f8a14);font-family:"Montserrat",sans-serif;font-size:23px;letter-spacing:1px;
  color:#214f06;line-height:40px}

.tabs{position:absolute;left:745px;top:701px;display:flex;gap:4px}
.tabs span{width:84px;height:39px;border-radius:5px 5px 0 0;font-size:12px;line-height:13px;padding:5px 0 0 16px}
.tabs .on{background:var(--green-dark);color:#fff}
.tabs .off{background:#dcdcdc;color:#777}
.post-list{position:absolute;left:745px;top:740px;width:314px;height:360px;border:2px solid var(--green-dark);
  border-radius:0 6px 6px 6px;background:#fff;padding:10px 14px 0}
.post-list li,.link-list li{list-style:none;font-size:12.2px;line-height:16px;color:var(--green-dark);
  border-bottom:1px solid var(--line);padding:6px 0 7px}
.post-list li:last-child{border-bottom:0}

.search{top:1137px;height:124px;background:linear-gradient(#ececec,#fbfbfb)}
.search .mag{position:absolute;left:18px;top:18px}
.widget-title{position:absolute;left:80px;top:18px;font-family:"Montserrat",sans-serif;font-size:20px;line-height:22px;color:#333}
.widget-title em{display:block;font-style:normal;color:var(--green)}
.search .box{position:absolute;left:14px;top:80px;width:288px;height:38px;border:1px solid #ccc;border-radius:4px;background:#f4f4f4;
  font-size:14px;line-height:36px;padding-left:40px;color:#777}
.search .go{position:absolute;right:3px;top:3px;width:58px;height:30px;border-radius:3px;background:var(--yellow);
  text-align:center;line-height:30px;font-weight:700;color:var(--ink)}
.link-list{position:absolute;left:765px;top:1292px;width:280px}
.link-list li{padding:4px 0 5px}

.categories{top:1479px;height:370px;background:linear-gradient(#ececec,#fbfbfb 90px,#fff 100px)}
.categories .horn{position:absolute;left:20px;top:26px;width:44px;height:34px}
.categories ul{position:absolute;left:20px;top:78px;width:280px}
.categories li{list-style:none;font-size:12.4px;line-height:17px;color:var(--ink);border-bottom:1px solid var(--line);padding:10px 0}

/* footer */
.site-footer{position:absolute;left:0;top:1892px;width:1200px;height:268px;background:#202020;border-top:5px solid var(--green)}
.email-art{position:absolute;left:142px;top:48px;width:100px;height:92px;border-radius:10px;background:linear-gradient(#3ab0e6,#1b77b8)}
.email-me{position:absolute;left:252px;top:66px;font-family:"Montserrat",sans-serif;font-weight:600;font-size:30px;line-height:32px;color:#fff}
.foot-h{position:absolute;font-family:"Montserrat",sans-serif;font-size:15px;color:var(--green-light)}
.follow-icons{position:absolute;left:138px;top:212px;display:flex;gap:12px}
.follow-icons span{width:30px;height:30px;border-radius:4px;background:#3d6fa8}
.foot-links{position:absolute;left:404px;top:66px;list-style:none}
.foot-links li{font-size:12.5px;color:#ddd;line-height:23.5px}
.foot-badge{position:absolute;width:28px;height:28px;border-radius:50%;background:#0d0d0d;border:2px solid #444}
.fan-box{position:absolute;left:548px;top:74px;width:228px;height:160px;background:#fff;border:1px solid #bbb;font-size:11px;color:#333}
.fan-box .head{display:flex;gap:8px;padding:8px}
.fan-box .dot{width:40px;height:40px;border-radius:50%;background:var(--ink)}
.fan-box .nm{font-weight:700;color:#3b5998;font-size:13px}
.fan-box .like{display:inline-block;margin-top:5px;border:1px solid #aab;background:#eef;padding:1px 6px;font-size:10px}
.fan-box .count{padding:0 8px;font-size:10.5px}
.fan-box .faces{display:flex;gap:6px;padding:4px 8px}
.fan-box .faces div{width:46px;text-align:center;font-size:8.5px;color:#666}
.fan-box .faces i{display:block;width:46px;height:44px;background:#b79a82}
.fan-box .plugin{position:absolute;bottom:0;left:0;right:0;border-top:1px solid #ddd;padding:2px 8px;font-size:8.5px;color:#666}
.join-title{position:absolute;left:836px;top:44px;font-family:"Montserrat",sans-serif;font-size:16px;line-height:20px;color:var(--green-light)}
.join-field{position:absolute;left:800px;top:92px;width:248px;height:50px;border:3px solid #666;border-radius:4px;background:#fff;
  font-size:14px;line-height:44px;padding-left:48px;color:#666}
.join-field svg{position:absolute;left:14px;top:15px}
.join-btn{position:absolute;left:800px;top:166px;width:172px;height:34px;border-radius:4px;background:var(--yellow);
  font-family:"Montserrat",sans-serif;font-size:14px;line-height:34px;text-align:center;color:var(--ink)}

.bottom{position:absolute;left:0;top:2160px;width:1200px;height:107px;background:linear-gradient(#e4e4e4,#f2f2f2)}
.bottom .brand{left:490px;top:18px;gap:10px}
.bottom .brand .mark{width:44px;height:44px}
.bottom .brand .name{font-size:29px;letter-spacing:-.5px}
.bottom .copy{position:absolute;left:0;width:1200px;top:78px;text-align:center;font-size:11.5px;color:#333}
</style>
</head>
<body>

<header class="site-header">
  <div class="social"><span></span><span></span><span></span><span></span><span></span></div>
  <div class="brand"><div class="mark"></div><div class="name">BellowMarsh</div></div>
  <div class="membership">
    <div class="l1">Membership to the</div>
    <div class="l2"><b>BellowMarsh</b> Community is FREE!</div>
  </div>
  <div class="signup-strip">
    <div class="avatar" role="img" aria-label="Small drawn figure inviting sign up"></div>
    <div class="email">your@email.com</div>
    <div class="btn">Sign Up Now</div>
  </div>
</header>

<nav class="main-nav">
  <ul>
    <li><div class="t">Home</div><div class="s">Back to Start</div></li>
    <li><div class="t">About</div><div class="s">Who is Reed?</div></li>
    <li><div class="t">Archives</div><div class="s">Hall of Records</div></li>
    <li><div class="t">Podcast</div><div class="s">PodShelf Broadcast</div></li>
    <li><div class="t">Videos</div><div class="s">How To Vids</div></li>
    <li><div class="t">Income Reports</div><div class="s">How I Make a Living Online</div></li>
    <li><div class="t">Resources</div><div class="s">Tools of the Trade</div></li>
    <li><div class="t">Contact</div><div class="s">Get a Hold of Me</div></li>
  </ul>
</nav>
<div class="updates">Get Updates via: (<a>Email</a> / <a>RSS</a>) <span class="rss"></span></div>

<main class="content-card">
  <h1>About Us</h1>
  <p>Lorem ipsum dolor sit amet, consectetur adipisicing elit, sed do eiusmod tempor incididunt ut labore et dolore magna aliqua. Ut enim ad minim veniam, quis nostrud exercitation ullamco laboris nisi ut aliquip ex ea commodo consequat. Duis aute irure dolor in reprehenderit in voluptate velit esse cillum dolore eu fugiat nulla pariatur. Excepteur sint occaecat cupidatat non proident, sunt in culpa qui officia deserunt mollit anim id est laborum.</p>
  <p>Sed ut perspiciatis unde omnis iste natus error sit voluptatem accusantium doloremque laudantium, totam rem aperiam, eaque ipsa quae ab illo inventore veritatis et quasi architecto beatae vitae dicta sunt explicabo. Nemo enim ipsam voluptatem quia voluptas sit aspernatur aut odit aut fugit, sed quia consequuntur magni dolores eos qui ratione voluptatem sequi nesciunt. Neque porro quisquam est, qui dolorem ipsum quia dolor sit amet, consectetur, adipisci velit, sed quia non numquam eius modi tempora incidunt ut labore et dolore magnam aliquam quaerat voluptatem. Ut enim ad minima veniam, quis nostrum exercitationem ullam corporis suscipit laboriosam, nisi ut aliquid ex ea commodi consequatur? Quis autem vel eum iure reprehenderit qui in ea voluptate velit esse quam nihil molestiae consequatur, vel illum qui dolorem eum fugiat quo voluptas nulla pariatur?</p>
  <p>Lorem ipsum dolor sit amet, consectetur adipisicing elit, sed do eiusmod tempor incididunt ut labore et dolore magna aliqua. Ut enim ad minim veniam, quis nostrud exercitation ullamco laboris nisi ut aliquip ex ea commodo consequat. Duis aute irure dolor in reprehenderit in voluptate velit esse cillum dolore eu fugiat nulla pariatur. Excepteur sint occaecat cupidatat non proident, sunt in culpa qui officia deserunt mollit anim id est laborum.</p>
  <p>Sed ut perspiciatis unde omnis iste natus error sit voluptatem accusantium doloremque laudantium, totam rem aperiam, eaque ipsa quae ab illo inventore veritatis et quasi architecto beatae vitae dicta sunt explicabo. Nemo enim ipsam voluptatem quia voluptas sit aspernatur aut odit aut fugit, sed quia consequuntur magni dolores eos qui ratione voluptatem sequi nesciunt. Neque porro quisquam est, qui dolorem ipsum quia dolor sit amet, consectetur, adipisci velit, sed quia non numquam eius modi tempora incidunt ut labore et dolore magnam aliquam quaerat voluptatem. Ut enim ad minima veniam, quis nostrum exercitationem ullam corporis suscipit laboriosam, nisi ut aliquid ex ea commodi consequatur? Quis autem vel eum iure reprehenderit qui in ea voluptate velit esse quam nihil molestiae consequatur, vel illum qui dolorem eum fugiat quo voluptas nulla pariatur?</p>
</main>

<aside>
  <section class="widget newsletter">
    <h2>Subscribe to Our<b>NEWSLETTER</b></h2>
    <div class="divider"></div>
    <div class="icon">
      <svg width="54" height="54" viewBox="0 0 54 54"><rect x="13" y="17" width="28" height="20" rx="2" fill="#fff" stroke="#c0392b" stroke-width="2"/><path d="M13 18 L27 29 L41 18" fill="none" stroke="#c0392b" stroke-width="2.5"/></svg>
    </div>
    <p>Lorem ipsum dolor sit amet, consectetur adipisicing elit, sed do eiusmod tempor incididunt ut labore et dolore.</p>
    <div class="field">Your Email Address</div>
    <div class="cta">SUBSCRIBE</div>
  </section>

  <div class="tabs"><span class="on">Most<br>Popular</span><span class="off">Hot<br>Posts</span></div>
  <ul class="post-list">
    <li>Lorem ipsum dolor sit amet, consectetur adipiscing elit.</li>
    <li>Mauris eu mauris sit amet libero commodo.</li>
    <li>Integer at velit urna, a ullamcorper purus.</li>
    <li>Duis at tellus nulla, vitae varius nisi.</li>
    <li>Proin eget libero ut nulla iaculis tempor.</li>
    <li>Pellentesque nec arcu eros, nec fermentum tortor.</li>
    <li>Nullam cursus pretium nibh, ut pellentesque massa egestas nec.</li>
    <li>Phasellus vehicula ligula in sapien mollis.</li>
    <li>Ut gravida ipsum quis enim pellentesque venenatis.</li>
  </ul>

  <section class="widget search">
    <svg class="mag" width="48" height="48" viewBox="0 0 48 48"><circle cx="19" cy="19" r="13" fill="#cfe6f5" stroke="#2a2a2a" stroke-width="5"/><path d="M29 29 L43 43" stroke="#2a2a2a" stroke-width="8" stroke-linecap="round"/></svg>
    <div class="widget-title">Search For<em>BellowMarsh</em></div>
    <div class="box">
      <svg class="abs" style="left:12px;top:11px" width="16" height="16" viewBox="0 0 16 16"><circle cx="6.5" cy="6.5" r="4.5" fill="none" stroke="#444" stroke-width="2"/><path d="M10 10 L14 14" stroke="#444" stroke-width="2.5"/></svg>
      Search<span class="go">Go!</span>
    </div>
  </section>
  <ul class="link-list">
    <li>Sed venenatis nulla in diam pellentes lacinia.</li>
    <li>Integer a eros at dolor vehicula euismod.</li>
    <li>Etiam et felis a nibh malesuada interdum.</li>
    <li>Maecenas et leo amet est egestas eleifend.</li>
    <li>Maecenas sed nibh lacus, sed blandit ipsum.</li>
    <li>Etiam et felis a nibh malesuada interdum.</li>
  </ul>

  <section class="widget categories">
    <svg class="horn" viewBox="0 0 44 34"><path d="M4 12 H14 L34 2 V32 L14 22 H4 Z" fill="#f08a1c"/><rect x="8" y="22" width="7" height="10" fill="#c96a0e"/></svg>
    <div class="widget-title" style="top:22px">Blog Post<em>Categories</em></div>
    <ul>
      <li>Lorem ipsum dolor sit amet, consectetur adipiscing elit.</li>
      <li>Donec vel velit non mauris ultrices eleifend nec ac dui.</li>
      <li>Nullam dapibus dolor vitae erat pharetra aliquam.</li>
      <li>In ac nulla quis magna lacinia vestibulum. Vivamus tincidunt nisl id erat laoreet tincidunt.</li>
      <li>Nulla molestie venenatis ligula, quis volutpat nulla commodo id.</li>
      <li>Pellentesque id dui non neque cursus venenatis.</li>
    </ul>
  </section>
</aside>

<footer class="site-footer">
  <div class="email-art" role="img" aria-label="Illustrated blue envelope character"></div>
  <div class="email-me">Email<br>Me</div>
  <div class="foot-h" style="left:139px;top:185px">Follow Us</div>
  <div class="follow-icons"><span></span><span></span><span></span><span></span><span></span></div>

  <div class="foot-h" style="left:404px;top:40px">Links</div>
  <ul class="foot-links">
    <li>Home</li><li>About</li><li>Archives</li><li>Podcast</li><li>Videos</li><li>Income Reports</li><li>Resources</li><li>Contact</li>
  </ul>

  <div class="foot-badge" style="left:548px;top:24px"></div>
  <div class="foot-h" style="left:588px;top:34px">Let's be friends?</div>
  <div class="fan-box">
    <div class="head"><div class="dot"></div><div><span class="nm">BellowMarsh</span> on FriendWall<br><span class="like">Like</span></div></div>
    <div class="count">247 people like <b>Marlo</b>.</div>
    <div class="faces">
      <div><i role="img" aria-label="Member profile photo"></i>Orin</div>
      <div><i role="img" aria-label="Member profile photo"></i>Teddy</div>
      <div><i role="img" aria-label="Member profile photo"></i>Lukas</div>
      <div><i role="img" aria-label="Member profile photo"></i>Milan</div>
    </div>
    <div class="plugin">FriendWall social plugin</div>
  </div>

  <div class="foot-badge" style="left:800px;top:24px"></div>
  <div class="join-title">FREE Membership For<br>BellowMarsh</div>
  <div class="join-field"><svg width="20" height="14" viewBox="0 0 20 14"><rect x="1" y="1" width="18" height="12" fill="none" stroke="#777" stroke-width="1.5"/><path d="M1 1 L10 8 L19 1" fill="none" stroke="#777" stroke-width="1.5"/></svg>Email</div>
  <div class="join-btn">Join The Revolution</div>
</footer>

<div class="bottom">
  <div class="brand"><div class="mark"></div><div class="name">BellowMarsh</div></div>
  <div class="copy">© 2012 BellowMarsh. All Rights Reserved.</div>
</div>

</body>
</html>
```